Physiotherapist for Horse and Rider

I need a web design and a working, functioning website for my profession as physiotherapist. Tabs available for the therapy I offer such a massage, stretching, taping, elektrotherapie en advies. Another tab for introducing myself and one for workshops I want to give. I like a tab for photo's and one for how the clients can contact me.

I like it similar too velnor.be Not too much text to read, a beautifull design with matching colours and nice photo's.

Target Market(s)

horse people

Industry/Entity Type

Massage

Number of Pages Required

1 page

Font styles to use
Serif
Script

Colors
34a6d7
0355a3
0493ce

Requirements
Must have
• I like the blue colours from my logo design.
• Contact with e-mail.
• domain name Brivo Lumé
Nice to have
• some off the photo's I uploaded

```html
<!DOCTYPE html>
<html lang="nl">
<head>
<meta charset="utf-8">
<title>Brivo Lumé – Kinesitherapie voor paard en ruiter</title>
<link href="https://fonts.googleapis.com/css2?family=Nunito+Sans:wght@400;600;700;800;900&display=swap" rel="stylesheet">
<style>
:root{
  --blue:#0493ce;
  --blue-light:#34a6d7;
  --blue-dark:#0355a3;
  --ink:#2b2b2b;
  --text:#555;
  --muted:#777;
  --grey-bg:#f5f5f5;
  --dark:#3b3b3d;
  --white:#fff;
}
*{box-sizing:border-box;margin:0;padding:0}
html,body{width:1200px;height:4082px;overflow:hidden}
body{position:relative;font-family:"Nunito Sans",Arial,sans-serif;color:var(--text);background:var(--white)}
section,header,footer{position:absolute;left:0;width:1200px}

/* header */
.site-header{top:0;height:142px;background:var(--white)}
.brand{position:absolute;left:95px;top:46px;display:flex;align-items:center;gap:12px;font-size:34px;font-weight:700;color:var(--blue-dark)}
.brand-dot{width:26px;height:26px;border-radius:50%;background:var(--blue)}
.main-nav{position:absolute;left:362px;top:68px;display:flex;gap:30px;font-size:15.5px;font-weight:600;color:var(--ink)}
.main-nav a{color:inherit;text-decoration:none;padding-bottom:10px}
.main-nav a.active{color:var(--blue);border-bottom:3px solid var(--blue)}

/* hero */
.hero{top:142px;height:660px;overflow:hidden}
.hero-photo{position:absolute;inset:0;background:linear-gradient(100deg,#2a2522 0%,#4a4038 35%,#6b6a5a 60%,#3d5a3a 80%,#2d2e2a 100%)}
.hero-shade{position:absolute;inset:0;background:rgba(0,0,0,.28)}
.hero-content{position:absolute;left:0;right:0;top:192px;text-align:center;color:var(--white)}
.hero-content h1{font-size:44px;font-weight:900;letter-spacing:1px}
.hero-content p{width:780px;margin:12px auto 0;font-size:19px;line-height:1.45}
.btn{display:inline-block;font-weight:800;text-transform:uppercase;text-decoration:none;letter-spacing:.5px}
.btn-solid{background:var(--blue);color:var(--white)}
.hero .btn{margin-top:32px;padding:12px 26px;font-size:19px}
.hero-dots{position:absolute;top:550px;left:0;right:0;display:flex;justify-content:center;gap:6px}
.hero-dots span{width:15px;height:15px;border-radius:50%;background:var(--white)}
.hero-dots span.current{background:transparent;border:2px solid var(--white)}
.hero-curve{position:absolute;left:0;bottom:0}

/* welcome */
.welcome{top:802px;height:505px;text-align:center}
.section-title{font-size:40px;font-weight:900;color:var(--ink);letter-spacing:.5px}
.welcome .section-title{margin-top:40px}
.welcome p{width:800px;margin:20px auto 0;font-size:14.5px;line-height:1.75;color:var(--muted)}
.welcome p + p{margin-top:20px}
.btn-outline{border:2px solid var(--blue-light);color:var(--blue);padding:13px 36px;font-size:19px;margin-top:40px}

/* band */
.band{top:1307px;height:503px;overflow:hidden}
.band-photo{position:absolute;inset:0;background:linear-gradient(90deg,#3f86b6 0%,#5ba1cc 40%,#69addb 65%,#4d93c3 100%)}
.band-content{position:absolute;left:0;right:0;top:122px;text-align:center;color:var(--white)}
.band-content h2{font-size:40px;font-weight:900}
.band-content p{width:870px;margin:22px auto 0;font-size:20px;line-height:1.55}

/* treatments */
.treatments{top:1810px;height:623px;text-align:center}
.treatments .section-title{margin-top:70px}
.treatment-list{display:flex;justify-content:center;gap:30px;margin-top:40px;list-style:none}
.treatment{width:180px}
.treatment-photo{width:160px;height:160px;margin:0 auto;border-radius:50%;border:9px solid var(--blue);background:linear-gradient(135deg,#8d7a68,#c4b6a4 55%,#6c5b4d)}
.treatment h3{margin-top:16px;font-size:20px;font-weight:800;color:var(--ink)}
.treatment p{width:160px;margin:6px auto 0;font-size:11px;line-height:1.55;color:var(--ink)}
.treatments .btn{margin-top:32px;padding:13px 38px;font-size:19px}

/* workshops */
.workshops{top:2433px;height:957px;background:var(--grey-bg);text-align:center}
.workshops .section-title{margin-top:72px}
.workshop-topics{margin-top:22px;font-size:19px;line-height:1.7;color:var(--ink)}
.workshop-frame{position:absolute;left:101px;top:274px;width:1003px;height:432px;background:var(--white);padding:12px;box-shadow:0 0 8px rgba(0,0,0,.12)}
.workshop-photo{width:100%;height:100%;background:linear-gradient(100deg,#6d6f6a 0%,#a79c8b 30%,#8b5a38 55%,#b7b3a6 80%,#7a7c77 100%)}
.workshops .lead{position:absolute;left:0;right:0;top:768px;width:920px;margin:0 auto;font-size:18.5px;line-height:1.65;color:var(--ink)}

/* contact */
.contact{top:3390px;height:624px;background:var(--dark);text-align:center;color:var(--white)}
.contact h2{margin-top:100px;font-size:40px;font-weight:900}
.contact .intro{margin-top:12px;font-size:14.5px}
.contact-form{position:absolute;left:101px;top:252px;width:1003px}
.field-row{display:flex;gap:19px}
.field{flex:1;height:44px;background:var(--white);color:#999;font-size:14px;text-align:left;padding:12px 10px}
.field-message{margin-top:21px;height:72px;background:var(--white);color:#999;font-size:14px;text-align:left;padding:10px}
.contact .btn{margin-top:38px;padding:14px 38px;font-size:18px}

/* footer */
.site-footer{top:4014px;height:68px;text-align:center;font-size:14px;color:var(--ink);padding-top:24px}
</style>
</head>
<body>

<header class="site-header">
  <div class="brand"><span class="brand-dot"></span>Brivo Lumé</div>
  <nav class="main-nav">
    <a class="active" href="#">Home</a>
    <a href="#">About Us</a>
    <a href="#">Massage</a>
    <a href="#">Stretching</a>
    <a href="#">Taping</a>
    <a href="#">Elektrotherapie en Advies</a>
    <a href="#">Photos</a>
    <a href="#">Contact Us</a>
  </nav>
</header>

<section class="hero">
  <div class="hero-photo" role="img" aria-label="Foto van de therapeute die een donker paard in de stal behandelt"></div>
  <div class="hero-shade"></div>
  <div class="hero-content">
    <h1>PHYSIOTHERAPIST</h1>
    <p>Als mens compenseren we jezelf vaak kleine ongemakken, waardoor er een onevenwicht ontstaat tussen bepaalde spieren. Dit heeft een effect op ons paard.</p>
    <a class="btn btn-solid" href="#">Get in touch</a>
  </div>
  <div class="hero-dots"><span class="current"></span><span></span><span></span></div>
  <svg class="hero-curve" width="1200" height="90" viewBox="0 0 1200 90" aria-hidden="true">
    <path d="M0 0 Q600 150 1200 0 L1200 90 L0 90 Z" fill="#fff"/>
  </svg>
</section>

<section class="welcome">
  <h2 class="section-title">WELCOME TO BRIVO LUMÉ</h2>
  <p>Lotte Maerens, 34 jaar, Brivo Lumé. Lotte studeerde af aan de Hogeschool Rivendaal als humaan kinesitherapeut in 2005. Zij begon onmiddellijk aan de opleiding Dierfysiotherapie in de Faculteit Dierwetenschappen te Velmaar en studeerde af als Fysiotherapeut voor paarden in 2008. Ze combineert beide als Kinesitherapeut voor Paard en Ruiter. Van jaar tot jaar schoolde ze zich bij in de Humane Manuele Therapie. In jaar leerde ze natuurlijk hoefbekappen. Sinds 2015 heeft ze zich ook verdiept in het Manueel Taping Concept en Paardtaping.</p>
  <p>Voeding is ook zeer belangrijk. Bepaalde voedingsstoffen worden makkelijker opgenomen dan andere. Bij belastende voeding kunnen maagklachten en darmproblemen ontstaan. Dit geeft het paard ongemak tijdens het rijden.</p>
  <a class="btn btn-outline" href="#">Read more</a>
</section>

<section class="band">
  <div class="band-photo" role="img" aria-label="Foto van een paard in de stal met blauwe kleurfilter"></div>
  <div class="band-content">
    <h2>KINESITHERAPIE VOOR PAARD EN RUITER</h2>
    <p>Een paard voelt een vlieg zitten op zijn vacht. Het kleinste onevenwicht in spierspanning kan hij dus voelen bij zijn ruiter. Paard en ruiter beïnvloeden elkaar, daarom behandel ik beide om zo tot een ontspannen geheel te komen, waarbij jij en je paard als één functioneren.</p>
  </div>
</section>

<section class="treatments">
  <h2 class="section-title">BEHANDELINGEN</h2>
  <ul class="treatment-list">
    <li class="treatment">
      <div class="treatment-photo" role="img" aria-label="Foto van een massagebehandeling bij een paard"></div>
      <h3>Massage</h3>
      <p>Heeft als doel de spieren te ontspannen en te versoepelen, de bloeddoorstroming te stimuleren, voedingsstoffen.</p>
    </li>
    <li class="treatment">
      <div class="treatment-photo" role="img" aria-label="Foto van het stretchen van een paardenbeen"></div>
      <h3>Stretching</h3>
      <p>Houdt de spieren en de pezen soepel en op lengte. Na een spierscheur wordt het nieuwe weefsel gevormd.</p>
    </li>
    <li class="treatment">
      <div class="treatment-photo" role="img" aria-label="Foto van elektrotherapie bij een paard"></div>
      <h3>Elektrotherapie</h3>
      <p>Pijnstillende stroom, genaamd TENS, geeft kleine trillingen in de spiervezels waardoor deze ontspannen.</p>
    </li>
    <li class="treatment">
      <div class="treatment-photo" role="img" aria-label="Foto van een getapet paard"></div>
      <h3>Taping</h3>
      <p>Door in het verloop van spieren te tapen, kan je de spier helpen ontspannen of net extra activeren.</p>
    </li>
    <li class="treatment">
      <div class="treatment-photo" role="img" aria-label="Foto van een zwart paard in de stal"></div>
      <h3>Advies</h3>
      <p>Tijdens een behandeling let ik ook op de stand van de benen en de staat van de hoeven. Ook het rijgewicht.</p>
    </li>
  </ul>
  <a class="btn btn-solid" href="#">More info</a>
</section>

<section class="workshops">
  <h2 class="section-title">WORKSHOPS</h2>
  <p class="workshop-topics">Zelf je paard masseren<br>Wellnessweekend voor paard en ruiter</p>
  <div class="workshop-frame">
    <div class="workshop-photo" role="img" aria-label="Foto van de therapeute die een bruin paard masseert tijdens een workshop"></div>
  </div>
  <p class="lead">Als kinesitherapeut ga ik op zoek naar de oorzaak van het probleem. In het begin kunnen er sommige symptomen zo drastisch aanwezig zijn dat ze de eigenlijke oorzaak maskeren. Dan moeten deze symptomen eerst behandeld worden, zodat de onderliggende oorzaak ontdekt kan worden.</p>
</section>

<section class="contact">
  <h2>CONTACT US</h2>
  <p class="intro">Contact us at the following for and General Enquiries</p>
  <form class="contact-form">
    <div class="field-row">
      <div class="field">First name</div>
      <div class="field">Last name</div>
      <div class="field">Email address</div>
      <div class="field">Phone number</div>
    </div>
    <div class="field-message">Message</div>
    <a class="btn btn-solid" href="#">Submit now !</a>
  </form>
</section>

<footer class="site-footer">© 2017 BRIVO LUMÉ . All right reserved . Term of Use</footer>

</body>
</html>
```